Kettle Ledger Business Card design

We need a stand out business card design for Accounting practice based in Australia specialising in pubs, clubs and hotels. We help venues maximise margins, create time and manage cashflow. One club we have been working with for the last 6 months has increased revenue by 3% and margin by 5% in this time frame. We have a back office outsourced system that costs less than having a full time employee and also allows the venues the added benefit of:<br/>-using the office space to become a revenue generating opportunity. <br/>-a complete system to enhance governance, accountability and efficiency within their operation<br/>-52 weeks cover so no hassle to cover annual/sick .. leave<br/><br/>We would like to see designs that use the colours of our logo (green & blue).
Target Market(s)
Australian Pubs, Clubs & Hotels abookkeeping, accounting and tax services
Industry/Entity Type
Accountant
Contact Information for Business Card
Miriam Oakley CPA
Principal
Accountant Tax Agent
Miriam@KettleLedger-example.com.au
0418693142
www.kettleledger-example.com.au
Accounting / Payroll / Tax / SMSF / Technology
Colors
Designer to choose colors to be used in the design.
Look and feel
Each slider illustrates characteristics of the customer's brand and the style your logo design should communicate.

```html
<!DOCTYPE html>
<html lang="en">
<head>
<meta charset="utf-8">
<title>Kettle Ledger Business Card</title>
<link rel="stylesheet" href="https://fonts.googleapis.com/css2?family=Montserrat:wght@400;500;700;800&display=swap">
<style>
  :root {
    --brand-blue: #1e3f87;
    --brand-green: #1c7a3e;
    --paper: #f2f3f3;
    --ink: #2a2a2a;
    --backdrop: #d9dadc;
    --white: #ffffff;
  }
  * { margin: 0; padding: 0; box-sizing: border-box; }
  html, body {
    width: 1200px;
    height: 1021px;
    overflow: hidden;
  }
  body {
    background: var(--backdrop);
    font-family: "Montserrat", sans-serif;
    position: relative;
  }
  .card {
    position: absolute;
    left: 250px;
    width: 700px;
    height: 420px;
    box-shadow: 0 6px 18px rgba(0, 0, 0, 0.18);
  }
  .card--front {
    top: 64px;
    background: var(--brand-blue);
    color: var(--white);
  }
  .card--back {
    top: 536px;
    background: var(--paper);
    color: var(--ink);
  }
  .wordmark {
    display: flex;
    align-items: center;
    gap: 18px;
  }
  .wordmark__dot {
    width: 46px;
    height: 46px;
    border-radius: 50%;
  }
  .wordmark__name {
    font-weight: 800;
    letter-spacing: -0.5px;
    white-space: nowrap;
  }
  .card--front .wordmark {
    position: absolute;
    left: 0;
    right: 0;
    top: 150px;
    justify-content: center;
  }
  .card--front .wordmark__dot { border: 4px solid var(--white); }
  .card--front .wordmark__name {
    font-size: 56px;
    color: var(--white);
  }
  .services {
    position: absolute;
    left: 0;
    right: 0;
    top: 322px;
    text-align: center;
    font-size: 17px;
    font-weight: 500;
    letter-spacing: 0.6px;
  }
  .card--back .wordmark {
    position: absolute;
    left: 48px;
    top: 46px;
  }
  .card--back .wordmark__dot {
    width: 40px;
    height: 40px;
    border: 4px solid var(--brand-green);
  }
  .card--back .wordmark__name {
    font-size: 44px;
    color: var(--brand-blue);
  }
  .person {
    position: absolute;
    left: 48px;
    top: 150px;
  }
  .person__name {
    font-size: 24px;
    font-weight: 800;
    color: var(--brand-blue);
    margin-bottom: 6px;
  }
  .person__role {
    font-size: 18px;
    line-height: 1.3;
  }
  .contact {
    position: absolute;
    left: 48px;
    top: 278px;
    list-style: none;
  }
  .contact__item {
    display: flex;
    align-items: center;
    gap: 10px;
    font-size: 18px;
    line-height: 1.55;
  }
  .contact__icon {
    width: 16px;
    height: 16px;
    flex: none;
  }
</style>
</head>
<body>

<section class="card card--front">
  <div class="wordmark">
    <span class="wordmark__dot"></span>
    <span class="wordmark__name">Kettle Ledger</span>
  </div>
  <p class="services">Accounting | Payroll | Tax | SMSF | Technology</p>
</section>

<section class="card card--back">
  <div class="wordmark">
    <span class="wordmark__dot"></span>
    <span class="wordmark__name">Kettle Ledger</span>
  </div>

  <div class="person">
    <h1 class="person__name">Miriam Oakley CPA</h1>
    <p class="person__role">Principal</p>
    <p class="person__role">Accountant Tax Agent</p>
  </div>

  <ul class="contact">
    <li class="contact__item">
      <svg class="contact__icon" viewBox="0 0 24 24" aria-hidden="true">
        <path fill="#1c7a3e" d="M6.6 10.8a15.1 15.1 0 0 0 6.6 6.6l2.2-2.2a1 1 0 0 1 1-.25 11.4 11.4 0 0 0 3.6.57 1 1 0 0 1 1 1V20a1 1 0 0 1-1 1A17 17 0 0 1 3 4a1 1 0 0 1 1-1h3.5a1 1 0 0 1 1 1c0 1.25.2 2.45.57 3.57a1 1 0 0 1-.25 1z"/>
      </svg>
      <span>0418693142</span>
    </li>
    <li class="contact__item">
      <svg class="contact__icon" viewBox="0 0 24 24" aria-hidden="true">
        <rect x="2" y="5" width="20" height="14" fill="none" stroke="#1c7a3e" stroke-width="2.4"/>
        <path d="M2 5l10 8 10-8" fill="none" stroke="#1c7a3e" stroke-width="2.4"/>
      </svg>
      <span>Miriam@KettleLedger-example.com.au</span>
    </li>
    <li class="contact__item">
      <svg class="contact__icon" viewBox="0 0 24 24" aria-hidden="true">
        <circle cx="12" cy="12" r="10" fill="none" stroke="#1c7a3e" stroke-width="2.2"/>
        <ellipse cx="12" cy="12" rx="4.5" ry="10" fill="none" stroke="#1c7a3e" stroke-width="2"/>
        <path d="M2 12h20M4 7h16M4 17h16" stroke="#1c7a3e" stroke-width="1.8"/>
      </svg>
      <span>www.kettleledger-example.com.au</span>
    </li>
  </ul>
</section>

</body>
</html>
```